I need a book cover for a 6x9 book. The front cover information (title and author) is below, and the back cover information will be given to the winning designer. I am wanting something vibrant and bright, and I am open to your creativity, but I do not want any pictures of people on the cover. Save room for the barcode on the back cover.
Title:
Psst! Then Where?
Open Doors, Warm Rooms: Ideas for Lively Evenings Ahead
Author:
Derrion Platt

```html
<!DOCTYPE html>
<html lang="en">
<head>
<meta charset="utf-8">
<title>Psst! Then Where? — Book Cover</title>
<link href="https://fonts.googleapis.com/css2?family=Bebas+Neue&family=Montserrat:wght@600&family=Cinzel:wght@600&family=Crimson+Pro:wght@400&display=swap" rel="stylesheet">
<style>
  :root {
    --page: #ffffff;
    --red: #f41c1e;
    --red-deep: #e3121a;
    --orange: #f26b0f;
    --glow: #fddb16;
    --glow-mid: #f98a1a;
    --cream: #f6e4c5;
    --ink: #0b0b0b;
    --title-edge: #f47a12;
    --bubble-text: #f9d9b4;
  }
  html, body {
    margin: 0;
    padding: 0;
    width: 1200px;
    height: 1200px;
    overflow: hidden;
    background: var(--page);
  }
  .cover {
    position: absolute;
    left: 221px;
    top: 32px;
    width: 764px;
    height: 1146px;
  }
  .cover svg { display: block; }
  .title-main { font-family: "Bebas Neue", "Oswald", sans-serif; }
  .subtitle { font-family: "Montserrat", "Questrial", sans-serif; font-weight: 600; }
  .bubble-word { font-family: "Crimson Pro", "Times New Roman", serif; }
  .author { font-family: "Cinzel", "Trajan Pro", serif; font-weight: 600; }
</style>
</head>
<body>
<div class="cover">
  <svg width="764" height="1146" viewBox="0 0 764 1146" xmlns="http://www.w3.org/2000/svg">
    <defs>
      <radialGradient id="cover-glow" cx="356" cy="545" r="520" gradientUnits="userSpaceOnUse">
        <stop offset="0" stop-color="var(--glow)"/>
        <stop offset="0.28" stop-color="var(--glow-mid)"/>
        <stop offset="0.7" stop-color="var(--red)"/>
        <stop offset="1" stop-color="var(--red)"/>
      </radialGradient>
    </defs>

    <!-- background -->
    <rect class="cover-bg" x="0" y="0" width="764" height="1146" fill="url(#cover-glow)"/>
    <rect class="base-band" x="0" y="1065" width="764" height="81" fill="var(--orange)"/>

    <!-- title panel -->
    <rect class="title-panel-shadow" x="48" y="68" width="663" height="460" rx="78" fill="var(--red-deep)"/>
    <rect class="title-panel" x="52" y="63" width="663" height="457" rx="78" fill="var(--cream)"/>

    <g class="title-main" font-size="282" fill="var(--ink)">
      <text x="100" y="320" textLength="562" lengthAdjust="spacingAndGlyphs" fill="var(--title-edge)">PSST!</text>
      <text x="97" y="316" textLength="562" lengthAdjust="spacingAndGlyphs">PSST!</text>
    </g>
    <g class="title-main" font-size="150" fill="var(--ink)">
      <text x="100" y="441" textLength="562" lengthAdjust="spacingAndGlyphs" fill="var(--title-edge)">THEN WHERE?</text>
      <text x="97" y="438" textLength="562" lengthAdjust="spacingAndGlyphs">THEN WHERE?</text>
    </g>
    <text class="subtitle" x="117" y="478" font-size="30" fill="var(--ink)" textLength="532" lengthAdjust="spacingAndGlyphs">Ideas for Lively Evenings Ahead</text>

    <!-- sketched speech bubbles artwork area -->
    <rect class="bubbles-art" x="110" y="590" width="548" height="366" rx="24" fill="var(--glow-mid)" opacity="0.35"
          role="img" aria-label="Hand-drawn outlined speech bubbles in cream with hatched shadows"/>
    <g class="bubble-word" fill="var(--bubble-text)" font-size="40">
      <text transform="translate(216 664) rotate(-15)" text-anchor="middle">Open</text>
      <text transform="translate(228 704) rotate(-15)" text-anchor="middle">Doors,</text>
      <text x="503" y="665" text-anchor="middle">Warm</text>
      <text x="503" y="704" text-anchor="middle">Rooms</text>
      <text transform="translate(202 870) rotate(-15)" text-anchor="middle" font-size="36">Then?</text>
      <text transform="translate(390 860) rotate(-20)" text-anchor="middle" font-size="34">Then</text>
      <text transform="translate(400 892) rotate(-20)" text-anchor="middle" font-size="34">Where?</text>
      <text transform="translate(592 862) rotate(-15)" text-anchor="middle" font-size="36">Where?</text>
    </g>

    <!-- author plate -->
    <rect class="author-plate-shadow" x="91" y="1025" width="584" height="90" rx="45" fill="var(--red-deep)"/>
    <rect class="author-plate" x="93" y="1021" width="582" height="88" rx="44" fill="var(--cream)"/>
    <text class="author" x="134" y="1088" font-size="62" fill="var(--ink)" textLength="502" lengthAdjust="spacingAndGlyphs">Derrion Platt</text>
  </svg>
</div>
</body>
</html>
```